Chia Seed Standup Pouch package design

We are looking for a clean and beautiful standup packaging design for our Organic Chia Seeds.

The package should have a healthy, natural, clean feel to it.

Please see attached Chia Seeds Packaging Samples for further instructions.

***** Requirements *****
- We want two bag style but one design. One will be with a spout and one without a spout.

- Print ready with bleed lines

Reason: We are extending the contest to allow for designers to perfect their designs. Some designs are coming real close to what we would be happy with. Price is now guaranteed. Thank you all for your designs.

Target Market(s)

Health and weight conscious individuals. Our target market are looking for whole natural foods.

Requirements
Must have
• - Include NFCB Organic logo (at minimum, can also include gluten free, vegan, etc)

On the back side of the package:
- have a place that promote our Chia Tea products. For example: "Also try our Natural Instant Chia Tea, made with Premium organic chia seeds and natural fruits and herbs extracts. (Chia Tea images attached)
Nice to have
• product highlights such as fiber, omega 3, protein, antioxidants, etc.

```html
<!DOCTYPE html>
<html lang="en">
<head>
<meta charset="utf-8">
<title>Verdel Nutrition – Organic Chia Seeds Pouch</title>
<link href="https://fonts.googleapis.com/css2?family=Oswald:wght@400;500;600&family=Satisfy&display=swap" rel="stylesheet">
<style>
  :root {
    --backdrop: #ffffff;
    --pouch-white: #f4f5f0;
    --green-light: #9ccc3c;
    --green-main: #7cb82f;
    --green-deep: #6aa626;
    --gold: #f2c81e;
    --gold-deep: #e5b512;
    --ink-dark: #3a3a1a;
    --white: #ffffff;
    --seed-dark: #55585a;
    --seed-light: #a9acad;
  }
  * { margin: 0; padding: 0; box-sizing: border-box; }
  html, body {
    width: 1200px; height: 675px; overflow: hidden;
    background: var(--backdrop);
  }
  .canvas {
    position: relative; width: 1200px; height: 675px;
    display: flex; align-items: center; justify-content: center;
  }
  .pouch {
    position: relative; width: 400px; height: 610px;
    border-radius: 6px; overflow: hidden;
    background: linear-gradient(180deg, var(--green-light) 0%, var(--green-main) 55%, var(--green-deep) 100%);
    box-shadow: 0 0 0 1px #e2e4dc;
    display: flex; flex-direction: column; align-items: center;
  }
  .pouch-top {
    width: 100%; height: 160px; background: var(--pouch-white);
    display: flex; align-items: center; justify-content: center;
  }
  .brand { display: flex; align-items: center; gap: 12px; color: var(--gold); }
  .brand-dot {
    width: 62px; height: 62px; border-radius: 50%; background: var(--gold);
  }
  .brand-name {
    font-family: "Oswald", sans-serif; font-weight: 500;
    line-height: 0.95; text-transform: uppercase;
  }
  .brand-name .line-one { display: block; font-size: 40px; letter-spacing: 1px; }
  .brand-name .line-two { display: block; font-size: 23px; letter-spacing: 1px; }
  .pouch-front {
    display: flex; flex-direction: column; align-items: center;
    padding-top: 40px; color: var(--white);
  }
  .claim {
    font-family: "Oswald", sans-serif; font-weight: 500;
    font-size: 17px; letter-spacing: 0.3px; text-transform: uppercase;
  }
  .product-name {
    font-family: "Satisfy", cursive; font-size: 58px; line-height: 1.05;
    margin-top: 2px;
  }
  .tagline {
    margin-top: 8px; padding: 4px 26px; border-radius: 8px;
    background: var(--gold); color: var(--ink-dark);
    font-family: "Oswald", sans-serif; font-weight: 600; font-size: 16px;
    letter-spacing: 0.6px; text-transform: uppercase;
  }
  .nutrition-facts {
    margin-top: 10px;
    font-family: "Oswald", sans-serif; font-weight: 500; font-size: 16px;
  }
  .seed-heart { margin-top: 12px; width: 150px; height: 136px; }
  .badges {
    display: flex; gap: 16px; margin-top: 16px;
  }
  .badge { display: flex; flex-direction: column; align-items: center; gap: 3px; width: 38px; }
  .badge-icon {
    width: 22px; height: 22px; border-radius: 50%;
    border: 1.5px solid var(--white);
  }
  .badge-icon.solid { background: var(--white); }
  .badge-label {
    font-family: "Oswald", sans-serif; font-size: 5.5px; font-weight: 500;
    text-transform: uppercase; text-align: center; white-space: nowrap;
  }
</style>
</head>
<body>
  <main class="canvas">
    <article class="pouch">
      <header class="pouch-top">
        <div class="brand">
          <span class="brand-dot"></span>
          <span class="brand-name">
            <span class="line-one">Verdel</span>
            <span class="line-two">Nutrition</span>
          </span>
        </div>
      </header>

      <section class="pouch-front">
        <p class="claim">100% Organic Raw</p>
        <h1 class="product-name">Chia Seeds</h1>
        <p class="tagline">Ancient Aztec Superfood</p>
        <p class="nutrition-facts">2.5 g Omega, 30 g Protein, 5 g Fiber</p>

        <svg class="seed-heart" viewBox="0 0 150 136" role="img" aria-label="Heart-shaped window filled with raw chia seeds">
          <defs>
            <linearGradient id="seedTone" x1="0" y1="0" x2="1" y2="1">
              <stop offset="0" stop-color="var(--seed-light)"/>
              <stop offset="0.5" stop-color="var(--seed-dark)"/>
              <stop offset="1" stop-color="var(--seed-light)"/>
            </linearGradient>
          </defs>
          <path d="M75 132 L10 58 C-6 38 6 6 36 6 C56 6 70 18 75 30 C80 18 94 6 114 6 C144 6 156 38 140 58 Z"
                fill="url(#seedTone)" stroke="var(--gold)" stroke-width="4" stroke-linejoin="round"/>
          <line x1="75" y1="30" x2="75" y2="132" stroke="var(--gold)" stroke-width="4"/>
        </svg>

        <ul class="badges">
          <li class="badge"><span class="badge-icon solid"></span><span class="badge-label">NFCB Certified</span></li>
          <li class="badge"><span class="badge-icon"></span><span class="badge-label">Vegetarian</span></li>
          <li class="badge"><span class="badge-icon"></span><span class="badge-label">GMO Free</span></li>
          <li class="badge"><span class="badge-icon"></span><span class="badge-label">Gluten Free</span></li>
          <li class="badge"><span class="badge-icon"></span><span class="badge-label">Vegan</span></li>
          <li class="badge"><span class="badge-icon"></span><span class="badge-label">Nothing Artificial</span></li>
        </ul>
      </section>
    </article>
  </main>
</body>
</html>
```